The 5 stages of grief experience

I'm an artist and I'm launching my art debut and i need a whole set of thing. I have the logo and the colors and the list of what I need:
Sponsorship proposal (I have the info to be pasted once design is ready)
Flyer for my art. It's about the 5 stages of grief and its like you go into a maze to go through each art instillation that takes you over each feeling, there is a lot of feelings and symmetry in the art.
Denial
Anger
Depression
Bargaining
Acceptance

Target Market(s)

Visual Art society

Font styles to use
Sans Serif

Colors
fee4d6
f8ba93
000000
5c5c5c
fbfbfb

Requirements
Must have
• Symmetry
• Feeling
• Strong message
• Bold
• An artistic idea I like a lot is a black and white moon changes and it's 5 different moons starting from a crescent ending in a full moon all next to each other or on top of each other and the phases underneath in small geometric font
Nice to have
• Softness
Should not have
• Femininity

```html
<!DOCTYPE html>
<html lang="en">
<head>
<meta charset="utf-8">
<title>The 5 Stages of Grief — Flyer</title>
<link rel="stylesheet" href="https://fonts.googleapis.com/css2?family=Antonio:wght@300;400;700&display=swap">
<style>
  :root {
    --peach-light: #fee4d6;
    --peach: #f8ba93;
    --ink: #000000;
    --slate: #5c5c5c;
    --paper: #fbfbfb;
    --maze-dark: #76675f;
    --maze-light: #fcd3bd;
    --list-ink: #464646;
    --stage: #ececec;
  }
  html, body {
    margin: 0;
    padding: 0;
    width: 1200px;
    height: 1200px;
    overflow: hidden;
    background: var(--stage);
  }
  .flyer {
    position: absolute;
    left: 210px;
    top: 50px;
    width: 779px;
    height: 1101px;
    box-shadow: 0 4px 14px rgba(0,0,0,0.18);
  }
  .flyer svg { display: block; }
  .type { font-family: "Antonio", sans-serif; }
  .brand-name { font-family: "Antonio", sans-serif; font-weight: 300; letter-spacing: 6px; }
</style>
</head>
<body>
  <div class="flyer">
    <svg width="779" height="1101" viewBox="0 0 779 1101" xmlns="http://www.w3.org/2000/svg">
      <!-- halves -->
      <rect class="half-dark" x="0" y="0" width="389" height="1101" fill="var(--slate)"/>
      <rect class="half-light" x="389" y="0" width="390" height="1101" fill="var(--peach-light)"/>

      <!-- artwork panels -->
      <rect class="artwork-dark" x="8" y="139" width="381" height="807" fill="var(--maze-dark)" opacity="0.55"
            role="img" aria-label="Dark maze pattern overlaid with a brushed portrait painting"/>
      <rect class="artwork-light" x="389" y="139" width="390" height="807" fill="var(--maze-light)" opacity="0.6"
            role="img" aria-label="Peach maze pattern overlaid with a brushed portrait painting"/>

      <!-- brand -->
      <circle class="brand-dot" cx="389" cy="147" r="66" fill="var(--ink)"/>
      <text class="brand-name" x="389" y="232" font-size="27" text-anchor="middle" fill="var(--ink)">ECHO</text>

      <!-- title -->
      <text class="type title-five" x="343" y="622" font-size="345" font-weight="700"
            textLength="89" lengthAdjust="spacingAndGlyphs" fill="var(--ink)">5</text>
      <text class="type title-the" x="288" y="551" font-size="58" font-weight="700"
            textLength="50" lengthAdjust="spacingAndGlyphs" fill="var(--ink)">THE</text>
      <text class="type title-stages" x="440" y="551" font-size="58" font-weight="700"
            textLength="115" lengthAdjust="spacingAndGlyphs" fill="var(--ink)">STAGES</text>
      <text class="type title-grief" x="440" y="609" font-size="58" font-weight="700"
            textLength="135" lengthAdjust="spacingAndGlyphs" fill="var(--ink)">OF GRIEF</text>

      <!-- stages list -->
      <g class="type stage-list" font-size="58" font-weight="400" fill="var(--list-ink)">
        <text x="393" y="686" textLength="105" lengthAdjust="spacingAndGlyphs">DENIAL</text>
        <text x="393" y="746" textLength="96" lengthAdjust="spacingAndGlyphs">ANGER</text>
        <text x="393" y="805" textLength="183" lengthAdjust="spacingAndGlyphs">DEPRESSION</text>
        <text x="393" y="865" textLength="176" lengthAdjust="spacingAndGlyphs">BARGAINING</text>
        <text x="393" y="925" textLength="184" lengthAdjust="spacingAndGlyphs">ACCEPTANCE</text>
      </g>

      <!-- event details -->
      <g class="type event-details" font-size="28" font-weight="400" fill="var(--peach-light)">
        <text x="68" y="1017" textLength="177" lengthAdjust="spacingAndGlyphs">APRIL 12.13.14</text>
        <text x="68" y="1051" textLength="237" lengthAdjust="spacingAndGlyphs">RAWAN ART GALLERY</text>
      </g>

      <!-- contact details -->
      <g class="type contact-details" font-size="28" font-weight="400" fill="var(--ink)">
        <text x="423" y="1003" textLength="272" lengthAdjust="spacingAndGlyphs">RIYADH, SAUDI ARABIA</text>
        <text x="423" y="1035" textLength="297" lengthAdjust="spacingAndGlyphs">ECHOEVENT.SA GMAIL.COM</text>
        <text x="423" y="1067" textLength="180" lengthAdjust="spacingAndGlyphs">966512348890</text>
      </g>
    </svg>
  </div>
</body>
</html>
```